ServLoom Website Homepage Design

Please provide your idea of homepage for a hosting company. This project is for DESIGN only, no coding.

It must use/combine colors used in logo, clean, modern look.

Homepage must consist of at least 4 sections (example: testimonials, services, and so on. not necesarily all of them). We would like the navigation to be horizontal, but not mandatory.

You can include a preview of services page (optional, not a must).

Number of Pages Required

1 page

Font styles to use
Sans Serif

```html
<!DOCTYPE html>
<html lang="en">
<head>
<meta charset="utf-8">
<title>ServLoom — Hosting Homepage</title>
<link href="https://fonts.googleapis.com/css2?family=Poppins:wght@400;500;600;700&display=swap" rel="stylesheet">
<style>
:root{
  --blue:#1a84e0;
  --blue-dark:#0f6cc0;
  --ink:#1b1f2e;
  --muted:#8a8f9c;
  --soft:#f2f6fd;
  --line:#e6eaf2;
  --footer:#0d1b33;
  --footer-bar:#12284a;
  --grey-btn:#9aa0a8;
}
*{box-sizing:border-box;margin:0;padding:0}
html,body{width:1200px;height:5021px;overflow:hidden}
body{font-family:'Poppins',sans-serif;color:var(--ink);background:#fff;position:relative}
.abs{position:absolute}
section,header,footer,.bar{position:absolute;left:0;width:1200px}
.accent{color:var(--blue)}
.lorem{font-size:13px;line-height:20px;color:var(--muted)}

/* top bar */
.topbar{top:0;height:34px;background:var(--blue);color:#fff;font-size:10px}
.topbar .mail{left:33px;top:10px}
.topbar .links{right:35px;top:10px;display:flex;gap:32px}

/* header */
.site-header{top:34px;height:79px;background:#fff}
.logo{font-size:25px;font-weight:600;letter-spacing:1px;color:var(--blue)}
.site-header .logo{left:35px;top:22px}
.lang{left:188px;top:31px;font-size:12px;font-weight:600;display:flex;gap:5px;align-items:center}
.nav{left:418px;top:30px;display:flex;gap:26px;font-size:12px;font-weight:500}
.nav .active{color:var(--blue)}
.search{left:826px;top:27px}
.call{left:874px;top:20px;display:flex;gap:10px;align-items:center}
.call b{display:block;font-size:13px;color:var(--blue);font-weight:600}
.call small{font-size:10px;color:var(--muted)}
.live-chat{left:1050px;top:19px;width:116px;height:40px;border-radius:20px;background:var(--blue);color:#fff;font-size:12px;font-weight:500;display:flex;align-items:center;justify-content:center}

/* hero */
.hero{top:113px;height:487px;background:var(--soft)}
.hero h1{left:123px;top:115px;font-size:45px;line-height:54px;font-weight:600;color:var(--blue)}
.hero p{left:123px;top:247px;font-size:17px;line-height:27px;color:#6b7080;width:470px}
.btn{display:flex;align-items:center;justify-content:center;border-radius:22px;color:#fff;font-size:12px;font-weight:500}
.hero .start{left:123px;top:329px;width:146px;height:40px;background:var(--blue)}
.hero .touch{left:282px;top:329px;width:146px;height:40px;background:var(--grey-btn)}
.hero-art{left:720px;top:62px;width:361px;height:390px;border-radius:24px;background:radial-gradient(circle at 60% 45%,#cfe6fb 0%,#e7f1fc 55%,rgba(242,246,253,0) 75%)}
.dropdown{top:113px;left:477px;width:172px;height:195px;background:#fff;box-shadow:0 6px 18px rgba(20,40,80,.12);padding:14px 18px;font-size:10px;color:#555;line-height:24.3px;z-index:5}

/* pricing */
.pricing{top:600px;left:33px;width:1132px;height:452px;display:flex;background:#fff;box-shadow:0 8px 28px rgba(20,40,80,.10)}
.plan{position:relative;width:283px;height:452px;border-right:1px solid var(--line);padding:0 14px}
.plan:last-child{border:none}
.plan.popular{box-shadow:0 10px 26px rgba(20,40,80,.14);z-index:2}
.ribbon{position:absolute;right:14px;top:0;width:22px;height:60px;background:var(--blue);color:#fff;font-size:8px;writing-mode:vertical-rl;text-align:center;padding-top:6px;clip-path:polygon(0 0,100% 0,100% 100%,50% 85%,0 100%)}
.plan h3{position:absolute;top:38px;left:14px;font-size:21px;font-weight:500}
.plan h3 span{color:var(--muted);font-weight:400}
.plan .desc{position:absolute;top:76px;left:14px;width:210px;font-size:11px;line-height:19px;color:var(--muted)}
.plan .rule{position:absolute;top:132px;left:14px;right:14px;border-top:1px solid var(--line)}
.price{position:absolute;top:158px;left:14px;display:flex;align-items:baseline;gap:2px}
.price s{font-size:19px;color:var(--muted)}
.price b{font-size:34px;font-weight:600;color:var(--blue)}
.price em{font-style:normal;font-size:11px;color:var(--muted)}
.sale{position:absolute;top:160px;right:16px;text-align:right;font-size:8px;color:var(--muted);line-height:16px}
.sale b{color:var(--blue);font-weight:600}
.features{position:absolute;top:234px;left:14px;list-style:none;font-size:10px;line-height:26px;color:#555}
.features li{display:flex;align-items:center;gap:7px}
.features b{color:var(--ink);font-weight:600}
.plan .buy{position:absolute;top:357px;left:14px;width:123px;height:35px;background:var(--blue)}

/* section heads */
.sec-title{left:0;width:1200px;text-align:center;font-size:34px;font-weight:600}
.sec-lead{left:275px;width:650px;text-align:center;font-size:15px;line-height:27px;color:var(--muted)}

/* hosting features */
.host-features{top:1161px;height:861px;background:var(--soft)}
.f-card{position:absolute;width:302px;height:239px;background:#fff;text-align:center;padding-top:23px}
.f-card.on{border-bottom:4px solid var(--blue)}
.ic-ring{width:82px;height:82px;border-radius:50%;border:2px solid var(--blue);margin:0 auto;display:flex;align-items:center;justify-content:center}
.f-card h4{font-size:19px;font-weight:500;margin-top:17px}
.f-card p{width:245px;margin:6px auto 0;font-size:12px;line-height:18px;color:var(--muted)}

/* specifications */
.specs{top:2022px;height:647px;background:#fff}
.tab{position:absolute;left:123px;width:214px;height:48px;background:#fff;box-shadow:0 4px 14px rgba(20,40,80,.07);font-size:13px;font-weight:600;display:flex;align-items:center;padding-left:16px}
.tab.on{color:var(--blue);border-left:3px solid var(--blue)}
.spec{position:absolute;width:346px;height:135px;border:1px solid var(--line);box-shadow:0 4px 14px rgba(20,40,80,.05);padding:20px 16px 0 72px}
.spec .ic{position:absolute;left:14px;top:34px}
.spec h5{font-size:16px;font-weight:600}
.spec p{font-size:12px;line-height:18px;color:var(--muted);margin-top:8px}

/* best services */
.best{top:2669px;height:715px;background:var(--soft)}
.s-card{position:absolute;top:267px;width:302px;height:304px;background:#fff;text-align:center;padding-top:33px}
.s-card h4{font-size:18px;font-weight:500}
.s-card .div{width:118px;margin:15px auto 19px;border-top:1px solid var(--line)}
.solid{width:82px;height:82px;border-radius:50%;background:var(--blue);margin:0 auto;display:flex;align-items:center;justify-content:center}
.s-card p{width:245px;margin:38px auto 0;font-size:12px;line-height:18px;color:var(--muted)}
.s-card a{display:block;margin-top:18px;font-size:11px;color:var(--blue);text-decoration:none}
.dots{left:0;width:1200px;display:flex;justify-content:center;gap:8px;align-items:center}
.dots i{width:6px;height:6px;border-radius:3px;background:var(--ink)}
.dots i.on{width:24px;background:var(--blue)}

/* process */
.process{top:3384px;height:524px;background:#fff}
.step{position:absolute;top:233px;width:340px;text-align:center}
.step .disc{width:102px;height:102px;border-radius:50%;background:#9ea2a8;margin:0 auto;position:relative;display:flex;align-items:center;justify-content:center}
.step .num{position:absolute;right:5px;top:-6px;width:30px;height:30px;border-radius:50%;background:var(--blue);color:#fff;font-size:12px;display:flex;align-items:center;justify-content:center;border:2px solid #fff}
.step h4{font-size:18px;font-weight:500;margin-top:34px}
.step p{width:300px;margin:6px auto 0;font-size:12px;line-height:18px;color:var(--muted)}

/* guarantee */
.guarantee{top:3908px;height:163px;background:var(--blue-dark);background:linear-gradient(90deg,#0f6fc6,#1580dc);color:#fff}
.guarantee h2{left:146px;top:39px;font-size:34px;font-weight:600}
.guarantee p{left:146px;top:97px;font-size:12px;font-weight:500}
.guarantee .more{left:910px;top:43px;width:146px;height:40px;background:#fff;color:var(--blue)}

/* testimonials */
.clients{top:4071px;height:614px;background:#fff}
.t-card{position:absolute;top:250px;width:302px;height:228px;background:#fff;box-shadow:0 6px 20px rgba(20,40,80,.08);padding:30px 15px 0}
.t-card h5{font-size:17px;font-weight:500}
.t-card small{font-size:10px;color:var(--blue)}
.avatar{position:absolute;right:22px;top:18px;width:64px;height:64px;border-radius:50%;background:linear-gradient(135deg,#e8d3c6,#c9a893)}
.t-card p{margin-top:38px;font-size:12px;line-height:18px;color:var(--muted);text-align:justify}
.quote{position:absolute;right:18px;bottom:18px;font-size:44px;line-height:30px;color:#c9dcf2;font-weight:700}

/* footer */
.site-footer{top:4685px;height:263px;background:var(--footer);color:#fff}
.site-footer .logo{left:33px;top:40px;color:#fff}
.about{left:33px;top:96px;width:250px;font-size:11px;line-height:18px}
.cards{left:33px;top:193px;display:flex;gap:5px}
.cards i{width:42px;height:28px;border-radius:3px;background:#fff}
.col{top:44px;font-size:11px;line-height:24.2px}
.col h6{font-size:17px;font-weight:500;color:var(--blue);margin-bottom:9px;line-height:24px}
.contact li{list-style:none;display:flex;gap:10px;margin-bottom:12px;line-height:17px}
.bottom{top:4948px;height:73px;background:var(--footer-bar);color:#fff;font-size:11px}
.bottom .copy{left:33px;top:29px}
.social{right:34px;top:22px;display:flex;gap:10px}
.social i{width:31px;height:31px;border-radius:50%;background:var(--blue)}
</style>
</head>
<body>

<div class="bar topbar">
  <div class="abs mail">✉&nbsp; info@example.com</div>
  <div class="abs links"><span>LOGIN</span><span>SUPPORT</span><span>CART</span></div>
</div>

<header class="site-header">
  <div class="abs logo">SERVLOOM</div>
  <div class="abs lang">
    <svg width="14" height="14" viewBox="0 0 14 14" fill="none" stroke="#1b1f2e" stroke-width="1.2"><circle cx="7" cy="7" r="6"/><path d="M1 7h12M7 1c3 3 3 9 0 12M7 1c-3 3-3 9 0 12"/></svg>US
  </div>
  <nav class="abs nav"><span>Home</span><span class="active">Hosting ⌄</span><span>Services ⌄</span><span>Pricing</span><span>Contact Us</span></nav>
  <svg class="abs search" width="24" height="24" viewBox="0 0 24 24" fill="none" stroke="#9aa0a8" stroke-width="2"><circle cx="10" cy="10" r="7"/><path d="M15 15l6 6"/></svg>
  <div class="abs call">
    <svg width="32" height="32" viewBox="0 0 24 24" fill="none" stroke="#1a84e0" stroke-width="1.5"><path d="M5 3h4l2 5-3 2a11 11 0 0 0 6 6l2-3 5 2v4a2 2 0 0 1-2 2A17 17 0 0 1 3 5a2 2 0 0 1 2-2z"/></svg>
    <div><b>(+1)123-456-789</b><small>Make a Call</small></div>
  </div>
  <div class="abs btn live-chat">Live Chat</div>
</header>

<div class="abs dropdown">Shared Hosting<br>Cloud Hosting<br>Dedicated Hosting<br>Reseller Hosting<br>Contact Us<br>Ctrl Panel Hosting<br>Vps Hosting</div>

<section class="hero">
  <h1 class="abs">Think beyond<br>Share Host!</h1>
  <p class="abs">Here is the infographic which gives some insights about the type of Web hosting.</p>
  <div class="abs btn start">Get Started</div>
  <div class="abs btn touch">Get In Touch</div>
  <div class="abs hero-art" role="img" aria-label="Illustration of a server rack, laptop and cloud connected by data lines"></div>
</section>

<div class="abs pricing">
  <div class="plan">
    <h3><b class="accent" style="font-weight:500">Personal</b> <span>Plans</span></h3>
    <p class="desc">We take pride providing secure Platform customers.</p>
    <div class="rule"></div>
    <div class="price"><s>$75</s><b>$30</b><em>/MO</em></div>
    <div class="sale">On Sale<br><b>SAVE 49%</b></div>
    <ul class="features">
      <li><svg width="11" height="11" viewBox="0 0 12 12"><circle cx="6" cy="6" r="5.5" fill="none" stroke="#1a84e0"/><path d="M3.5 6l2 2 3-4" fill="none" stroke="#1a84e0" stroke-width="1.3"/></svg><b>CPU:</b> 2 Cores</li>
      <li><svg width="11" height="11" viewBox="0 0 12 12"><circle cx="6" cy="6" r="5.5" fill="none" stroke="#1a84e0"/><path d="M3.5 6l2 2 3-4" fill="none" stroke="#1a84e0" stroke-width="1.3"/></svg><b>RAM:</b> 4 GB</li>
      <li><svg width="11" height="11" viewBox="0 0 12 12"><circle cx="6" cy="6" r="5.5" fill="none" stroke="#1a84e0"/><path d="M3.5 6l2 2 3-4" fill="none" stroke="#1a84e0" stroke-width="1.3"/></svg><b>DISK:</b> (128GB - 256GB) SSD</li>
      <li><svg width="11" height="11" viewBox="0 0 12 12"><circle cx="6" cy="6" r="5.5" fill="none" stroke="#1a84e0"/><path d="M3.5 6l2 2 3-4" fill="none" stroke="#1a84e0" stroke-width="1.3"/></svg><b>UPLINK:</b> 1Gbps - 20TB</li>
    </ul>
    <div class="btn buy">Purchase Now!</div>
  </div>
  <div class="plan">
    <h3><b class="accent" style="font-weight:500">Basic</b> <span>Plans</span></h3>
    <p class="desc">We take pride providing secure Platform customers.</p>
    <div class="rule"></div>
    <div class="price"><s>$85</s><b>$49</b><em>/MO</em></div>
    <div class="sale">On Sale<br><b>SAVE 49%</b></div>
    <ul class="features">
      <li><svg width="11" height="11" viewBox="0 0 12 12"><circle cx="6" cy="6" r="5.5" fill="none" stroke="#1a84e0"/><path d="M3.5 6l2 2 3-4" fill="none" stroke="#1a84e0" stroke-width="1.3"/></svg><b>CPU:</b> 2 Cores</li>
      <li><svg width="11" height="11" viewBox="0 0 12 12"><circle cx="6" cy="6" r="5.5" fill="none" stroke="#1a84e0"/><path d="M3.5 6l2 2 3-4" fill="none" stroke="#1a84e0" stroke-width="1.3"/></svg><b>RAM:</b> 4 GB</li>
      <li><svg width="11" height="11" viewBox="0 0 12 12"><circle cx="6" cy="6" r="5.5" fill="none" stroke="#1a84e0"/><path d="M3.5 6l2 2 3-4" fill="none" stroke="#1a84e0" stroke-width="1.3"/></svg><b>DISK:</b> (128GB - 256GB) SSD</li>
      <li><svg width="11" height="11" viewBox="0 0 12 12"><circle cx="6" cy="6" r="5.5" fill="none" stroke="#1a84e0"/><path d="M3.5 6l2 2 3-4" fill="none" stroke="#1a84e0" stroke-width="1.3"/></svg><b>UPLINK:</b> 1Gbps - 20TB</li>
    </ul>
    <div class="btn buy">Purchase Now!</div>
  </div>
  <div class="plan popular">
    <div class="ribbon">Popular</div>
    <h3><b class="accent" style="font-weight:500">Standard</b> <span>Plans</span></h3>
    <p class="desc">We take pride providing secure Platform customers.</p>
    <div class="rule"></div>
    <div class="price"><s>$90</s><b>$75</b><em>/MO</em></div>
    <div class="sale">On Sale<br><b>SAVE 49%</b></div>
    <ul class="features">
      <li><svg width="11" height="11" viewBox="0 0 12 12"><circle cx="6" cy="6" r="5.5" fill="none" stroke="#1a84e0"/><path d="M3.5 6l2 2 3-4" fill="none" stroke="#1a84e0" stroke-width="1.3"/></svg><b>CPU:</b> 4 Cores</li>
      <li><svg width="11" height="11" viewBox="0 0 12 12"><circle cx="6" cy="6" r="5.5" fill="none" stroke="#1a84e0"/><path d="M3.5 6l2 2 3-4" fill="none" stroke="#1a84e0" stroke-width="1.3"/></svg><b>RAM:</b> 8 GB</li>
      <li><svg width="11" height="11" viewBox="0 0 12 12"><circle cx="6" cy="6" r="5.5" fill="none" stroke="#1a84e0"/><path d="M3.5 6l2 2 3-4" fill="none" stroke="#1a84e0" stroke-width="1.3"/></svg><b>DISK:</b> (256GB - 500GB) SSD</li>
      <li><svg width="11" height="11" viewBox="0 0 12 12"><circle cx="6" cy="6" r="5.5" fill="none" stroke="#1a84e0"/><path d="M3.5 6l2 2 3-4" fill="none" stroke="#1a84e0" stroke-width="1.3"/></svg><b>UPLINK:</b> 2Gbps - 40TB</li>
    </ul>
    <div class="btn buy">Purchase Now!</div>
  </div>
  <div class="plan">
    <h3><b class="accent" style="font-weight:500">Premium</b> <span>Plans</span></h3>
    <p class="desc">We take pride providing secure Platform customers.</p>
    <div class="rule"></div>
    <div class="price"><s>$100</s><b>$80</b><em>/MO</em></div>
    <div class="sale">On Sale<br><b>SAVE 49%</b></div>
    <ul class="features">
      <li><svg width="11" height="11" viewBox="0 0 12 12"><circle cx="6" cy="6" r="5.5" fill="none" stroke="#1a84e0"/><path d="M3.5 6l2 2 3-4" fill="none" stroke="#1a84e0" stroke-width="1.3"/></svg><b>CPU:</b> 2 Cores</li>
      <li><svg width="11" height="11" viewBox="0 0 12 12"><circle cx="6" cy="6" r="5.5" fill="none" stroke="#1a84e0"/><path d="M3.5 6l2 2 3-4" fill="none" stroke="#1a84e0" stroke-width="1.3"/></svg><b>RAM:</b> 4 GB</li>
      <li><svg width="11" height="11" viewBox="0 0 12 12"><circle cx="6" cy="6" r="5.5" fill="none" stroke="#1a84e0"/><path d="M3.5 6l2 2 3-4" fill="none" stroke="#1a84e0" stroke-width="1.3"/></svg><b>DISK:</b> (128GB - 256GB) SSD</li>
      <li><svg width="11" height="11" viewBox="0 0 12 12"><circle cx="6" cy="6" r="5.5" fill="none" stroke="#1a84e0"/><path d="M3.5 6l2 2 3-4" fill="none" stroke="#1a84e0" stroke-width="1.3"/></svg><b>UPLINK:</b> 1Gbps - 20TB</li>
    </ul>
    <div class="btn buy">Purchase Now!</div>
  </div>
</div>

<section class="host-features">
  <h2 class="abs sec-title" style="top:80px">We Provide <span class="accent">Hosting</span> Features</h2>
  <p class="abs sec-lead" style="top:145px">Lorem ipsum dolor sit amet, consectetur adipiscing elit. Cras ut massa turpis. Phasellus eget tellus eros. Nulla ullamcorper sollicitudin velit, a porta mauris vestibulum ac. Nulla at tellus et arcu venenatis tempus.</p>

  <div class="f-card" style="left:123px;top:267px"><div class="ic-ring"><svg width="38" height="38" viewBox="0 0 24 24" fill="none" stroke="#1a84e0" stroke-width="1.2"><rect x="4" y="4" width="16" height="11" rx="1"/><path d="M9 19h6M12 15v4"/></svg></div><h4>Domain Sale</h4><p>Lorem ipsum dolor sit amet, consectetur adipiscing elit. Morbi porttitor ipsum ut efficitur commodo.</p></div>
  <div class="f-card on" style="left:448px;top:267px"><div class="ic-ring"><svg width="38" height="38" viewBox="0 0 24 24" fill="none" stroke="#1a84e0" stroke-width="1.2"><path d="M7 16a4 4 0 0 1 0-8 5 5 0 0 1 9.5-1A4 4 0 0 1 17 16z"/><path d="M12 16v4"/></svg></div><h4>Cloud Hosting</h4><p>Lorem ipsum dolor sit amet, consectetur adipiscing elit. Morbi porttitor ipsum ut efficitur commodo.</p></div>
  <div class="f-card" style="left:773px;top:267px"><div class="ic-ring"><svg width="38" height="38" viewBox="0 0 24 24" fill="none" stroke="#1a84e0" stroke-width="1.2"><circle cx="12" cy="10" r="6"/><path d="M6 10h12M12 4v12M6 20h12"/></svg></div><h4>VPS Hosting</h4><p>Lorem ipsum dolor sit amet, consectetur adipiscing elit. Morbi porttitor ipsum ut efficitur commodo.</p></div>
  <div class="f-card" style="left:123px;top:522px"><div class="ic-ring"><svg width="38" height="38" viewBox="0 0 24 24" fill="none" stroke="#1a84e0" stroke-width="1.2"><rect x="9" y="3" width="6" height="5"/><rect x="3" y="15" width="6" height="5"/><rect x="15" y="15" width="6" height="5"/><path d="M12 8v4M6 15v-3h12v3"/></svg></div><h4>Shared Hosting</h4><p>Lorem ipsum dolor sit amet, consectetur adipiscing elit. Morbi porttitor ipsum ut efficitur commodo.</p></div>
  <div class="f-card" style="left:448px;top:522px"><div class="ic-ring"><svg width="38" height="38" viewBox="0 0 24 24" fill="none" stroke="#1a84e0" stroke-width="1.2"><rect x="3" y="4" width="18" height="12" rx="1"/><path d="M8 20h8M12 16v4M10.5 11l1.5-3 1.5 3z"/></svg></div><h4>Linux Hosting</h4><p>Lorem ipsum dolor sit amet, consectetur adipiscing elit. Morbi porttitor ipsum ut efficitur commodo.</p></div>
  <div class="f-card" style="left:773px;top:522px"><div class="ic-ring"><svg width="38" height="38" viewBox="0 0 24 24" fill="none" stroke="#1a84e0" stroke-width="1.2"><circle cx="12" cy="11" r="7"/><path d="M5 11h14M12 4c3 3 3 11 0 14M12 4c-3 3-3 11 0 14M8 21h8"/></svg></div><h4>Web Security</h4><p>Lorem ipsum dolor sit amet, consectetur adipiscing elit. Morbi porttitor ipsum ut efficitur commodo.</p></div>
</section>

<section class="specs">
  <h2 class="abs sec-title" style="top:80px">Our Hosting <span class="accent">Specifications</span></h2>
  <p class="abs sec-lead" style="top:145px">Lorem ipsum dolor sit amet, consectetur adipiscing elit. Cras ut massa turpis. Phasellus eget tellus eros. Nulla ullamcorper sollicitudin velit, a porta mauris vestibulum ac.</p>

  <div class="tab" style="top:272px">Hosting Software</div>
  <div class="tab" style="top:340px">Hosting Database</div>
  <div class="tab on" style="top:407px">Additional Software</div>
  <div class="tab" style="top:475px">Hosting Security</div>

  <div class="spec" style="left:366px;top:269px"><svg class="ic" width="46" height="46" viewBox="0 0 24 24" fill="none" stroke="#1a84e0" stroke-width="1"><rect x="3" y="5" width="18" height="13" rx="1"/><circle cx="12" cy="11.5" r="3"/><path d="M8 21h8"/></svg><h5>1-Click App Marketplace</h5><p>Lorem ipsum dolor sit amet, consectetur adipiscing elit. Morbi porttitor ipsum ut efficitur commodo.</p></div>
  <div class="spec" style="left:730px;top:269px"><svg class="ic" width="46" height="46" viewBox="0 0 24 24" fill="none" stroke="#1a84e0" stroke-width="1"><circle cx="12" cy="10" r="6"/><path d="M6 10h12M12 4v12M5 20h14M12 16v4"/></svg><h5>Global Availability</h5><p>Lorem ipsum dolor sit amet, consectetur adipiscing elit. Morbi porttitor ipsum ut efficitur commodo.</p></div>
  <div class="spec" style="left:366px;top:419px"><svg class="ic" width="46" height="46" viewBox="0 0 24 24" fill="none" stroke="#1a84e0" stroke-width="1"><rect x="3" y="5" width="18" height="13" rx="1"/><circle cx="12" cy="11.5" r="3"/><path d="M8 21h8"/></svg><h5>Hostnotes in Minutes</h5><p>Lorem ipsum dolor sit amet, consectetur adipiscing elit. Morbi porttitor ipsum ut efficitur commodo.</p></div>
  <div class="spec" style="left:730px;top:419px"><svg class="ic" width="46" height="46" viewBox="0 0 24 24" fill="none" stroke="#1a84e0" stroke-width="1"><circle cx="12" cy="10" r="6"/><path d="M6 10h12M12 4v12M5 20h14M12 16v4"/></svg><h5>Flexible Compute Types</h5><p>Lorem ipsum dolor sit amet, consectetur adipiscing elit. Morbi porttitor ipsum ut efficitur commodo.</p></div>
</section>

<section class="best">
  <h2 class="abs sec-title" style="top:80px">We Provide <span class="accent">Best</span> Services</h2>
  <p class="abs sec-lead" style="top:145px">Lorem ipsum dolor sit amet, consectetur adipiscing elit. Cras ut massa turpis. Phasellus eget tellus eros. Nulla ullamcorper sollicitudin velit, a porta mauris vestibulum ac. Nulla at tellus et arcu venenatis tempus.</p>

  <div class="s-card" style="left:123px"><h4>Automatic Scalability</h4><div class="div"></div><div class="solid"><svg width="40" height="40" viewBox="0 0 24 24" fill="none" stroke="#fff" stroke-width="1.2"><rect x="4" y="5" width="16" height="11" rx="1"/><circle cx="12" cy="10.5" r="2.5"/><path d="M8 20h8"/></svg></div><p>Lorem ipsum dolor sit amet, consectetur adipiscing elit. Morbi porttitor ipsum ut efficitur commodo.</p><a>Read More..</a></div>
  <div class="s-card" style="left:448px"><h4>E-Mail Hosting</h4><div class="div"></div><div class="solid"><svg width="40" height="40" viewBox="0 0 24 24" fill="none" stroke="#fff" stroke-width="1.2"><rect x="5" y="4" width="14" height="5"/><rect x="5" y="10" width="14" height="5"/><rect x="5" y="16" width="14" height="4"/></svg></div><p>Lorem ipsum dolor sit amet, consectetur adipiscing elit. Morbi porttitor ipsum ut efficitur commodo.</p><a>Read More..</a></div>
  <div class="s-card" style="left:773px"><h4>Daily Backup</h4><div class="div"></div><div class="solid"><svg width="40" height="40" viewBox="0 0 24 24" fill="none" stroke="#fff" stroke-width="1.2"><rect x="4" y="4" width="12" height="9"/><rect x="9" y="11" width="11" height="9"/></svg></div><p>Lorem ipsum dolor sit amet, consectetur adipiscing elit. Morbi porttitor ipsum ut efficitur commodo.</p><a>Read More..</a></div>

  <div class="abs dots" style="top:601px"><i></i><i class="on"></i><i></i></div>
</section>

<section class="process">
  <h2 class="abs sec-title" style="top:84px">Website Hosting <span class="accent">Process</span></h2>
  <p class="abs sec-lead" style="top:148px">Lorem ipsum dolor sit amet, consectetur adipiscing elit. Cras ut massa turpis. Phasellus eget tellus eros. Nulla ullamcorper sollicitudin.</p>

  <svg class="abs" style="left:365px;top:264px" width="140" height="40" viewBox="0 0 140 40" fill="none" stroke="#1b1f2e" stroke-width="1.3" stroke-dasharray="4 4"><path d="M4 30C40 0 100 0 132 34"/><path d="M124 32l8 4-1-9" stroke-dasharray="none"/></svg>
  <svg class="abs" style="left:698px;top:264px" width="140" height="40" viewBox="0 0 140 40" fill="none" stroke="#1b1f2e" stroke-width="1.3" stroke-dasharray="4 4"><path d="M4 8C40 38 100 38 132 6"/><path d="M125 6l8-1-1 8" stroke-dasharray="none"/></svg>

  <div class="step" style="left:99px"><div class="disc"><span class="num">1</span><svg width="40" height="40" viewBox="0 0 24 24" fill="none" stroke="#fff" stroke-width="1.2"><rect x="4" y="5" width="16" height="11" rx="1"/><circle cx="12" cy="10.5" r="2.5"/><path d="M8 20h8"/></svg></div><h4>Register Domain Name</h4><p>Lorem ipsum dolor sit amet, consectetur adipiscing elit. Morbi porttitor ipsum ut efficitur commodo.</p></div>
  <div class="step" style="left:430px"><div class="disc"><span class="num">2</span><svg width="40" height="40" viewBox="0 0 24 24" fill="none" stroke="#fff" stroke-width="1.2"><rect x="4" y="5" width="16" height="11" rx="1"/><circle cx="12" cy="10.5" r="2.5"/><path d="M8 20h8"/></svg></div><h4>Hosting A Website</h4><p>Lorem ipsum dolor sit amet, consectetur adipiscing elit. Morbi porttitor ipsum ut efficitur commodo.</p></div>
  <div class="step" style="left:761px"><div class="disc"><span class="num">3</span><svg width="40" height="40" viewBox="0 0 24 24" fill="none" stroke="#fff" stroke-width="1.2"><rect x="4" y="5" width="16" height="11" rx="1"/><circle cx="12" cy="10.5" r="2.5"/><path d="M8 20h8"/></svg></div><h4>Upload Website To Server</h4><p>Lorem ipsum dolor sit amet, consectetur adipiscing elit. Morbi porttitor ipsum ut efficitur commodo.</p></div>
</section>

<section class="guarantee">
  <h2 class="abs">30 Days Money-Back Guarantee</h2>
  <p class="abs">If you're not 100% satisfied with ServLoom, we'll refund your payment. No hassle, no risk.</p>
  <div class="abs btn more">Read More</div>
</section>

<section class="clients">
  <h2 class="abs sec-title" style="top:82px">What Our <span class="accent">Clients</span> Says</h2>
  <p class="abs sec-lead" style="top:147px">Lorem ipsum dolor sit amet, consectetur adipiscing elit. Cras ut massa turpis. Phasellus eget tellus eros. Nulla ullamcorper sollicitudin velit.</p>

  <div class="t-card" style="left:123px"><h5>John Doe</h5><small>CEO, NORTHWIND</small><div class="avatar" role="img" aria-label="Client portrait photo"></div><p>Lorem ipsum dolor sit amet, consectetur adipiscing elit. Nunc faucibus, erat vitae commodo varius, ex velit pretium ipsum, cursus cursus ipsum nisl nec augue. quis malesuada quam aliquet et.</p><span class="quote">“</span></div>
  <div class="t-card" style="left:448px"><h5>John Doe</h5><small>CEO, NORTHWIND</small><div class="avatar" role="img" aria-label="Client portrait photo"></div><p>Lorem ipsum dolor sit amet, consectetur adipiscing elit. Nunc faucibus, erat vitae commodo varius, ex velit pretium ipsum, cursus cursus ipsum nisl nec augue. quis malesuada quam aliquet et.</p><span class="quote">“</span></div>
  <div class="t-card" style="left:773px"><h5>John Doe</h5><small>CEO, NORTHWIND</small><div class="avatar" role="img" aria-label="Client portrait photo"></div><p>Lorem ipsum dolor sit amet, consectetur adipiscing elit. Nunc faucibus, erat vitae commodo varius, ex velit pretium ipsum, cursus cursus ipsum nisl nec augue. quis malesuada quam aliquet et.</p><span class="quote">“</span></div>

  <div class="abs dots" style="top:514px"><i></i><i class="on"></i><i></i></div>
</section>

<footer class="site-footer">
  <div class="abs logo">SERVLOOM</div>
  <p class="abs about">Lorem ipsum dolor sit amet, consectetur adipiscing elit. Cras ut massa turpis. Phasellus eget tellus eros. Nulla ullamcorper sollicitudin velit, a porta mauris vestibulum ac.</p>
  <div class="abs cards"><i></i><i></i><i></i><i></i></div>

  <div class="abs col" style="left:321px"><h6>Our Services</h6>PressKit Hosting<br>Shared Hosting<br>Dedicated Hosting<br>Managed Hosting<br>Cloud Hosting<br>Reseller Hosting</div>
  <div class="abs col" style="left:553px"><h6>Quick Links</h6>Terms of Service<br>Privacy Policy<br>FAQ<br>Contact Us<br>Support Center<br>Knowledgebase</div>
  <div class="abs col" style="left:773px"><h6>Security</h6>Terms of Service<br>Privacy Policy<br>FAQ<br>Contact Us<br>Support Center<br>Knowledgebase</div>
  <div class="abs col" style="left:953px;width:220px"><h6>Contact</h6>
    <ul class="contact">
      <li><svg width="12" height="14" viewBox="0 0 12 14" fill="#fff"><path d="M6 0a5 5 0 0 1 5 5c0 4-5 9-5 9S1 9 1 5a5 5 0 0 1 5-5zm0 3a2 2 0 1 0 0 4 2 2 0 0 0 0-4z"/></svg><span>418 Harbor Lane, Westfield Park<br>Los Angeles, US</span></li>
      <li><svg width="12" height="12" viewBox="0 0 24 24" fill="#fff"><path d="M5 2h4l2 5-3 2a11 11 0 0 0 6 6l2-3 5 2v4a2 2 0 0 1-2 2A18 18 0 0 1 3 4a2 2 0 0 1 2-2z"/></svg><span>+1-123-456-789</span></li>
      <li><svg width="13" height="10" viewBox="0 0 13 10" fill="#fff"><path d="M0 0h13v10H0zM1 1l5.5 4L12 1z" fill-rule="evenodd"/></svg><span>info@example.com</span></li>
    </ul>
  </div>
</footer>

<div class="bar bottom">
  <div class="abs copy">Copyright 2021 ServLoom All Rights Reserved.</div>
  <div class="abs social"><i></i><i></i><i></i><i></i></div>
</div>

</body>
</html>
```